【 概要 】 広告看板に使用するためのイラストデザイン を募集します。 【 依頼内容 】 ・サイズ: A3(人物の全身のサイズ) ・作成数: 1種類 ・利用用途:看板 【 デザインイメージ 】 アニメ OWL×GARDENの父のような、イメージで 日本人によせて男前にしていただければと思います。 (髪の毛を黒)(目の色)など 制服、ポーズ(ハーネスの色は黄色)は添付資料にてご確認下さい。 【 契約金額(税抜) 】 3万円 ※契約金額(税込)からシステム利用料を差し引いた金額が、ワーカーさまの受取金額となります その他ご質問等ありましたら、気軽にお問い合わせください。 ご応募をお待ちしております! |
どの案も素敵でしたので、社内にて協議した結果こちらの作品にて決定させていただきます。
沢山のご応募ありがとうございました。
また、制作物の際は宜しくお願いします。

```html
<!DOCTYPE html>
<html lang="ja">
<head>
<meta charset="utf-8">
<title>フルハーネス型墜落制止用器具 完全装着</title>
<link rel="stylesheet" href="https://fonts.googleapis.com/css2?family=Noto+Sans+JP:wght@700;900&display=swap">
<style>
  :root {
    --stripe-green: #169a3e;
    --stripe-yellow: #f4e60a;
    --panel-white: #ffffff;
    --header-green: #17a043;
    --ink-black: #0a0a0a;
    --text-white: #ffffff;
    --figure-blue: #6f9fd4;
    --figure-blue-dark: #3f6fa8;
    --harness-yellow: #f2d21c;
  }
  html, body {
    margin: 0;
    padding: 0;
    width: 1200px;
    height: 840px;
    overflow: hidden;
    background: var(--panel-white);
  }
  .poster {
    position: relative;
    width: 1200px;
    height: 840px;
    overflow: hidden;
    font-family: "Noto Sans JP", sans-serif;
    background: var(--panel-white);
  }
  .hazard-band {
    position: absolute;
    top: 0;
    height: 840px;
    background: repeating-linear-gradient(
      45deg,
      var(--stripe-green) 0 34px,
      var(--stripe-yellow) 34px 68px
    );
  }
  .hazard-band--left { left: 0; width: 144px; }
  .hazard-band--right { right: 0; width: 156px; }
  .content-panel {
    position: absolute;
    left: 144px;
    top: 0;
    width: 900px;
    height: 840px;
    background: var(--panel-white);
  }
  .worker-figure {
    position: absolute;
    left: 80px;
    top: 40px;
    width: 340px;
    height: 780px;
    border-radius: 150px 150px 24px 24px;
    background: linear-gradient(180deg, var(--figure-blue) 0%, var(--harness-yellow) 45%, var(--figure-blue) 55%, var(--figure-blue-dark) 100%);
  }
  .speech-bubble {
    position: absolute;
    left: 310px;
    top: 12px;
    width: 130px;
    height: 150px;
  }
  .speech-bubble svg { position: absolute; inset: 0; }
  .speech-bubble__text {
    position: absolute;
    left: 0;
    top: 16px;
    width: 130px;
    height: 120px;
    writing-mode: vertical-rl;
    display: flex;
    align-items: center;
    justify-content: center;
    font-weight: 900;
    font-size: 24px;
    line-height: 1.15;
    color: var(--ink-black);
  }
  .product-header {
    position: absolute;
    left: 476px;
    top: 0;
    width: 550px;
    height: 196px;
    background: var(--header-green);
    display: flex;
    flex-direction: column;
    align-items: center;
    justify-content: center;
    color: var(--text-white);
    font-weight: 900;
    font-size: 68px;
    line-height: 1.12;
    letter-spacing: 2px;
  }
  .headline {
    position: absolute;
    left: 476px;
    width: 550px;
    margin: 0;
    text-align: center;
    font-weight: 900;
    font-size: 260px;
    line-height: 1;
    letter-spacing: 0;
    white-space: nowrap;
    color: var(--ink-black);
  }
  .headline--top { top: 250px; }
  .headline--bottom { top: 548px; }
</style>
</head>
<body>
  <main class="poster">
    <div class="hazard-band hazard-band--left"></div>
    <div class="content-panel"></div>
    <div class="hazard-band hazard-band--right"></div>

    <div class="worker-figure" role="img" aria-label="フルハーネスとヘルメットを着用し、ランヤードを手に持つ青い作業服姿の作業員のイラスト"></div>

    <div class="speech-bubble">
      <svg width="130" height="150" viewBox="0 0 130 150" aria-hidden="true">
        <path d="M65 4 C110 4 126 30 126 70 C126 112 104 136 65 136 L40 146 L46 130 C18 120 4 100 4 70 C4 30 20 4 65 4 Z" fill="#fff" stroke="#0a0a0a" stroke-width="4"/>
      </svg>
      <div class="speech-bubble__text">大切な命、<br>守ろう！</div>
    </div>

    <header class="product-header">
      <span>フルハーネス型</span>
      <span>墜落制止用器具</span>
    </header>

    <h1 class="headline headline--top">完全</h1>
    <p class="headline headline--bottom">装着</p>
  </main>
</body>
</html>
```